Website Landing Page for Marlowe Systems

Create a custom designed website landing page for our business. Looking for a professional upscale design that incorporates our logo and logo colors into the theme. I want a standard fixed frame website, not a constant scrolling format that seems to be the trend. To start with I'm looking for more of the graphic design part, maybe a concept or theme, I don't expect to see a finished project. Not interested in generic templates or layouts.

The name of our company is Marlowe Systems and I've attached our logo below. I'd like to have the web page have the same look and feel of our logo, as well as the colors. Our company, Marlowe Systems does system design, installation, and programming, of residential and commercial Audio/Video and Automation systems. We do home theaters, lighting and building automation, video conferencing systems, security camera installations, conference rooms, projectors, distributed audio systems, and similar Technology projects. This will be a professional services/informational website. We will not sell products on this website. This website will be used to advertise our company and communicate our services to prospective customers. Having a well designed, professional and clean website is one way we want to distinguish our company from the competition.

Here are some examples of what I consider a professional well designed website
http://www.qrzstudio.example/Work/

Last year we had our tradeloft store designed (with PixelHarbor) and I'm really happy with the way it turned out. You can see it at www.KelpGearDepot.example I consider this to be a great design and looking for the same level of quality with this new website. However, do not copy or use any part of this design in this new project. This tradeloft store is completely separate from our other company Marlowe Systems. I only mention this tradeloft store an an example of good work.

Target Market(s)

People interested in Audio/Video, home theaters, home automation. We do sales, system design, and programming. We typically work on larger projects with both residential and commercial customers.

Industry/Entity Type

Business

Number of Pages Required

1 page

Requirements
Must have
• Great design elements. Please use a white background. I think white goes well with our logo colors.

```html
<!DOCTYPE html>
<html lang="en">
<head>
<meta charset="utf-8">
<title>Marlowe Systems</title>
<link href="https://fonts.googleapis.com/css2?family=Source+Sans+3:ital,wght@0,400;0,600;0,700;1,400&display=swap" rel="stylesheet">
<style>
:root{
  --blue:#5a8ac3;
  --blue-band:rgba(64,118,186,.82);
  --green:#45b512;
  --green-text:#3fae14;
  --ink:#222;
  --grey:#555;
  --soft-grey:#6a6a6a;
  --rule:#c9d3e0;
  --top-band:#c8cbe6;
  --footer-dark:#102a44;
  --white:#fff;
}
*{box-sizing:border-box;margin:0;padding:0}
html,body{width:1200px;height:2700px;overflow:hidden;background:var(--white)}
body{position:relative;font-family:"Source Sans 3",Arial,sans-serif;color:var(--ink)}
.abs{position:absolute}

/* header */
.top-band{left:0;top:0;width:1200px;height:23px;background:var(--top-band)}
.site-header{left:0;top:23px;width:1200px;height:102px;background:rgba(255,255,255,.94)}
.brand{left:25px;top:15px;display:flex;align-items:center;gap:14px}
.brand-dot{width:72px;height:72px;border-radius:50%;background:var(--blue)}
.brand-name{font-size:22px;font-weight:700;color:var(--blue);line-height:1.1;width:140px}
.main-nav a{position:absolute;top:44px;font-size:20px;font-weight:600;color:#333;text-decoration:none;letter-spacing:.3px}

/* hero */
.hero{left:0;top:125px;width:1200px;height:678px;
  background:linear-gradient(180deg,#8fa6c4 0%,#b9c6d6 30%,#6f8a58 52%,#4d7a34 75%,#5f8a69 100%)}
.hero-title{left:0;width:1200px;top:450px;text-align:center;color:var(--white);font-size:31px;font-weight:700;line-height:40px;letter-spacing:.3px}
.hero-tag{left:0;width:1200px;top:546px;text-align:center;color:var(--white);font-size:34px;font-style:italic}
.btn{display:flex;align-items:center;justify-content:center;background:var(--green);color:var(--white);font-weight:700;border-radius:5px;text-decoration:none}
.hero-btn{left:516px;top:606px;width:199px;height:62px;font-size:23px}

/* products */
.section-title{left:0;width:1200px;top:880px;text-align:center;color:var(--blue);font-size:50px;font-weight:600;letter-spacing:1px}
.section-sub{left:0;width:1200px;top:942px;text-align:center;color:var(--soft-grey);font-size:31px;font-style:italic}
.section-copy{left:115px;width:970px;top:990px;text-align:center;color:var(--grey);font-size:26px;line-height:31px}
.tile{width:351px;height:219px}
.tile-label{position:absolute;left:0;bottom:0;width:100%;height:44px;background:var(--blue-band);color:var(--white);font-size:26px;font-weight:600;text-align:center;line-height:44px;letter-spacing:.5px}
.t-conf{background:linear-gradient(160deg,#8a5a44,#c9b8a6 55%,#3c3a3a)}
.t-theater{background:linear-gradient(160deg,#e6d3a8,#b88a52 55%,#6d4f33)}
.t-security{background:linear-gradient(160deg,#d8b478,#a47a3e 55%,#6e5530)}
.t-lighting{background:linear-gradient(160deg,#3c3b3e,#6e6a62 55%,#2a2422)}
.t-projection{background:linear-gradient(160deg,#d9d9dc,#8d8f96 55%,#4a4c55)}
.t-buildings{background:linear-gradient(160deg,#5d8fd4,#3b6fb5 55%,#7aa7e0)}

/* news */
.news-title{left:47px;top:1665px;color:var(--blue);font-size:35px;font-weight:600;letter-spacing:.5px}
.news-item{left:43px;width:390px}
.news-date{font-size:17px;color:#222}
.news-text{font-size:16.5px;font-style:italic;line-height:21px;color:#333;margin-top:5px}
.read-more{position:absolute;font-size:15px;font-weight:700;color:var(--green-text);text-decoration:underline}
.news-rule{left:23px;width:382px;height:2px;background:var(--rule)}
.news-more{left:186px;top:2222px;display:flex;align-items:center;gap:8px;color:var(--blue);font-size:15px;font-weight:600}
.feature-img{left:468px;top:1679px;width:732px;height:302px;background:linear-gradient(180deg,#9fb3cb 0%,#d2dbe4 45%,#8fa0ab 68%,#5a7a3c 100%)}
.feature-title{left:470px;top:2000px;font-size:21px;font-weight:700}
.feature-quote{left:470px;top:2036px;width:700px;font-size:21px;line-height:24px;color:#333}
.feature-btn{left:470px;top:2131px;width:138px;height:45px;font-size:19px}

/* footer */
.site-footer{left:0;top:2318px;width:1200px;height:382px;background:linear-gradient(135deg,#1b4468 0%,var(--footer-dark) 45%,#1a4a6a 100%);color:var(--white)}
.f-name{left:18px;top:60px;font-size:27px;font-weight:700}
.f-line{left:24px;font-size:20px}
.f-link{color:var(--green-text);text-decoration:underline;font-size:18px}
.f-btn{left:14px;top:267px;width:138px;height:47px;font-size:20px}
.f-head{font-size:25px;font-weight:700;color:var(--green-text)}
.f-item{font-size:19px;color:var(--white)}
.social{left:1032px;top:304px;display:flex;gap:8px}
.social span{width:27px;height:27px;background:var(--green);border-radius:3px}
.f-legal{left:0;width:1200px;top:342px;display:flex;justify-content:center;gap:24px;font-size:14px;padding-left:120px}
.f-legal a{color:var(--white);text-decoration:underline}
</style>
</head>
<body>

<div class="abs top-band"></div>
<header class="abs site-header">
  <div class="abs brand"><span class="brand-dot"></span><span class="brand-name">Marlowe Systems</span></div>
  <nav class="main-nav">
    <a style="left:432px">Home</a>
    <a style="left:547px">Who we are</a>
    <a style="left:717px">Our Products</a>
    <a style="left:898px">Services</a>
    <a style="left:1044px">Contact</a>
  </nav>
</header>

<section>
  <div class="abs hero" role="img" aria-label="City skyline behind a park with trees and a canal"></div>
  <h1 class="abs hero-title">Lorem ipsum dolor sit amet, consectetur adipiscing<br>elit. Vestibulum vel lacus id mauris suscipit</h1>
  <p class="abs hero-tag">Marlowe Systems are for you</p>
  <a class="abs btn hero-btn">learn more</a>
</section>

<section>
  <h2 class="abs section-title">Experience our Products</h2>
  <p class="abs section-sub">Marlowe Systems are for you</p>
  <p class="abs section-copy">Lorem ipsum dolor sit amet, consectetur adipiscing elit. Ut viverra dolor pulvinar, semper justo at, euismod tortor. Morbi pretium convallis urna, eget tempus massa mattis sit amet. Suspendisse vel tellus tortor.</p>

  <div class="abs tile t-conf" style="left:80px;top:1128px" role="img" aria-label="Conference room with long table and wall screen"><span class="tile-label">Conferencing System</span></div>
  <div class="abs tile t-theater" style="left:431px;top:1128px" role="img" aria-label="Home theater living room with large screen"><span class="tile-label">Home Theater</span></div>
  <div class="abs tile t-security" style="left:782px;top:1128px" role="img" aria-label="Ornate hall interior with columns"><span class="tile-label">Security System</span></div>
  <div class="abs tile t-lighting" style="left:80px;top:1347px" role="img" aria-label="Bar interior with lighting"><span class="tile-label">Lighting Automation</span></div>
  <div class="abs tile t-projection" style="left:431px;top:1347px" role="img" aria-label="Lecture hall with projection screen"><span class="tile-label">Projection</span></div>
  <div class="abs tile t-buildings" style="left:782px;top:1347px" role="img" aria-label="Glass office tower against blue sky"><span class="tile-label">Buildings</span></div>
</section>

<section>
  <h2 class="abs news-title">News and Information</h2>

  <article class="abs news-item" style="top:1732px">
    <p class="news-date">June 12, 2017</p>
    <p class="news-text">Lorem ipsum dolor sit amet, consectetur adipiscing elit. Ut viverra dolor pulvinar, semper justo at, euismod tortor. Morbi pretium convallis urna, eget tempus massa mattis sit amet. Suspendisse vel tellus tortor.</p>
    <a class="read-more" style="left:4px;top:142px">Read More</a>
  </article>
  <div class="abs news-rule" style="top:1910px"></div>

  <article class="abs news-item" style="top:1930px">
    <p class="news-date">June 17, 2017</p>
    <p class="news-text">Lorem ipsum dolor sit amet, consectetur adipiscing elit. Ut viverra dolor pulvinar, semper justo at, euismod tortor. Morbi pretium convallis urna.</p>
    <a class="read-more" style="left:4px;top:111px">Read More</a>
  </article>
  <div class="abs news-rule" style="top:2077px"></div>

  <article class="abs news-item" style="top:2083px">
    <p class="news-date">June 17, 2017</p>
    <p class="news-text">Lorem ipsum dolor sit amet, consectetur adipiscing elit. Ut viverra dolor pulvinar, semper justo at, euismod tortor. Morbi pretium convallis urna.</p>
    <a class="read-more" style="left:4px;top:106px">Read More</a>
  </article>

  <div class="abs news-more">
    <svg width="20" height="11" viewBox="0 0 20 11"><path d="M0 0h20L10 11z" fill="#8fa9cf"/></svg>
    <span>More</span>
  </div>

  <div class="abs feature-img" role="img" aria-label="City skyline with tall towers above a tree line"></div>
  <h3 class="abs feature-title">Lorem Ipsum</h3>
  <p class="abs feature-quote">“Lorem ipsum dolor sit amet, consectetur adipiscing elit. Ut viverra dolor pulvinar, semper justo at, euismod tortor. Morbi pretium convallis urna, eget tempus massa mattis sit amet. “</p>
  <a class="abs btn feature-btn">Learn More</a>
</section>

<footer class="abs site-footer" role="img" aria-label="Dark blue view of a glass office building under cloudy sky">
  <p class="abs f-name">Marlowe Systems</p>
  <p class="abs f-line" style="top:100px">48 Alder Row</p>
  <p class="abs f-line" style="top:126px">Fernvale, CA 90000</p>
  <p class="abs f-line" style="top:162px;font-size:18px">(555) 010-0142</p>
  <p class="abs f-line" style="top:187px;font-size:18px">(555) 010-0142</p>
  <a class="abs f-link" style="left:20px;top:219px">Get Directions</a>
  <a class="abs btn f-btn">Contact</a>

  <p class="abs f-head" style="left:505px;top:62px">About</p>
  <p class="abs f-item" style="left:505px;top:104px">History</p>
  <p class="abs f-item" style="left:505px;top:141px">The team</p>
  <p class="abs f-item" style="left:505px;top:178px">Careers</p>

  <p class="abs f-head" style="left:686px;top:62px">Services</p>
  <p class="abs f-item" style="left:688px;top:101px;font-size:18px">Installations</p>
  <p class="abs f-item" style="left:688px;top:136px;font-size:18px">Commercial</p>
  <p class="abs f-item" style="left:690px;top:173px;font-size:18px">Residential</p>
  <p class="abs f-item" style="left:690px;top:208px;font-size:18px">Project Management</p>

  <p class="abs f-head" style="left:927px;top:64px">Products</p>
  <p class="abs f-item" style="left:929px;top:109px;font-size:18px">Projection</p>
  <p class="abs f-item" style="left:929px;top:146px;font-size:18px">Home Theater</p>
  <p class="abs f-item" style="left:929px;top:181px;font-size:18px">Buildings</p>
  <p class="abs f-item" style="left:929px;top:214px;font-size:18px">Conferencing System</p>
  <p class="abs f-item" style="left:929px;top:251px;font-size:18px">Security System</p>

  <div class="abs social"><span></span><span></span><span></span><span></span></div>

  <div class="abs f-legal"><span>All Rights Reserved</span><a>Privacy Policy</a><a>Terms of Use</a></div>
</footer>

</body>
</html>
```